Business Card Design

I would like a new business card design for an accounting firm that specializes in resolving clients tax problems. I want the card to give the impression that we are not your typical stodgy accounting firm, but at the same time we will get the job done.
Industry/Entity Type
Business
Contact Information for Business Card
Dorian T Welsby
Certified Public Accountant
38-27 52nd Street
Sunnyside, NY 11287
Tel: (718) 555-0142
Fax: (888) 555-0199
e-mail: dtwthecpa@ledgerpost.com
website: harborfilingreliefexperts.com

```html
<!DOCTYPE html>
<html lang="en">
<head>
<meta charset="utf-8">
<title>Dorian T Welsby — Business Card</title>
<link rel="stylesheet" href="https://fonts.googleapis.com/css2?family=Signika:wght@300;400;700&display=swap">
<style>
  :root {
    --card-bg: #ffffff;
    --ink: #111111;
    --accent: #0b9ad8;
  }
  * { margin: 0; padding: 0; box-sizing: border-box; }
  html, body {
    width: 1200px;
    height: 704px;
    overflow: hidden;
    background: var(--card-bg);
  }
  .card {
    position: relative;
    width: 1200px;
    height: 704px;
    background: var(--card-bg);
    font-family: "Signika", sans-serif;
    color: var(--ink);
  }
  .card__line {
    position: absolute;
    left: 344px;
    white-space: nowrap;
    line-height: 1;
  }
  .card__name {
    top: 106px;
    font-size: 52px;
    font-weight: 700;
    letter-spacing: 0.5px;
  }
  .card__title {
    top: 177px;
    font-size: 37px;
    font-weight: 400;
    color: var(--accent);
    letter-spacing: 0.6px;
  }
  .card__detail {
    font-size: 37px;
    font-weight: 300;
    letter-spacing: 0.4px;
  }
  .card__label {
    color: var(--accent);
  }
  .card__address { top: 260px; }
  .card__tel     { top: 321px; }
  .card__fax     { top: 381px; }
  .card__email   { top: 441px; }
  .card__web     { top: 554px; }
</style>
</head>
<body>
  <main class="card">
    <h1 class="card__line card__name">Dorian T Welsby</h1>
    <p class="card__line card__title">Certified Public Accountant</p>
    <p class="card__line card__detail card__address">38-27 52nd Street Sunnyside, NY 11287</p>
    <p class="card__line card__detail card__tel"><span class="card__label">Tel:</span> (718) 555-0142</p>
    <p class="card__line card__detail card__fax"><span class="card__label">Fax:</span> (888) 555-0199</p>
    <p class="card__line card__detail card__email"><span class="card__label">e-mail:</span> dtwthecpa@ledgerpost.com</p>
    <p class="card__line card__detail card__web">www.harborfilingreliefexperts.com</p>
  </main>
</body>
</html>
```